依頼詳細
■依頼詳細
モノトーンでシック・スタイリッシュに、トップページの情報はコンパクトに見せたいと思っております。

■ホームページに期待する効果
L既存顧客の満足度向上
L問い合わせ数の向上
L認知度の向上
L売上の向上

■ターゲット
・男女比|3:7
・30代メイン
・会社員、自営業、主婦、学生、子ども

■コンテンツ素材
Lロゴ
L写真データ>HPからも引用OK

■デザインのテイスト
シンプル、知性的、シック、クール

■希望デザインカラー
白、黒のモノトーン

■参考サイト
http://www.tokuri-style.example/
→色使いが好き。構成は見にくい。

http://bomvel.example.jp/
→雰囲気好き、情報をコンパクトにまとめているのが良い

http://pelkon517.example/
→色使いが好き。構成は縦に長すぎる。

※好きな雑誌の雰囲気
velune
MARTHA
大人ORCA

■SNS関連
・インスタグラム
・ノートラインへのリンク
https://noteline.example/

■サイトマップ
①Home
②Menu
③Staff
④Salon
⑤Blog(一覧) (詳細)
⑥News(一覧) (詳細)
⑦Gallery(一覧)
⑧Recommend
⑨Access
⑩Guest Snap
⑪Recruit
⑫Product
⑬Contact
⑭Calendar
http://www.dun-ket-semo.example/index
白黒
●写真・素材
1)内観・外観写真
枚数が多いため、以下のURLよりダウンロードをお願い致します。

http://filevault.example.jp/download/9c3b7e2d51a8f04c62e1d9b7a35c08e4f2d6b1a7
ダウンロードパスワード kmt3r415

2)その他素材
今回、ピクセラ「https://jp.pixera.example/」というサイトにて 制作中の間定期契約を致しました。
デザインの際には、一度仮素材にて配置を頂き、ピクセラ以外の素材は無料の物をご使用頂きたいです。
たくさんのご提案ありがとうございます!

さらなる提案を見てみたいため募集期間延長致します。
宜しくお願い致します。

画像をうまく活用していただき、かっこいいデザインです。
大変気に入りました。

こちらの意図を組んでいただいたデザイン、ありがとうございます!

```html
<!DOCTYPE html>
<html lang="ja">
<head>
<meta charset="utf-8">
<title>VEL hair salon</title>
<link href="https://fonts.googleapis.com/css2?family=Noto+Sans+JP:wght@400;700&family=Noto+Serif:wght@400;700&display=swap" rel="stylesheet">
<style>
:root{
  --ink:#111;
  --paper:#fff;
  --mist:#ececec;
  --line:#cfcfcf;
  --muted:#555;
}
*{box-sizing:border-box;margin:0;padding:0}
html,body{width:1200px;height:2664px;overflow:hidden;background:var(--paper);color:var(--ink);font-family:"Noto Sans JP",sans-serif}
.page{position:relative;width:1200px;height:2664px}
.header{position:absolute;left:100px;top:16px;width:1000px;height:120px}
.brand{position:absolute;left:0;top:28px;display:flex;align-items:center;gap:14px;color:var(--ink)}
.brand-mark{width:22px;height:22px;background:currentColor}
.brand-name{font-family:"Noto Serif",serif;font-weight:700;font-size:44px;line-height:1;letter-spacing:3px}
.contact{position:absolute;right:0;top:22px;font-family:"Noto Serif",serif;font-weight:700}
.contact .addr{font-size:15px}
.contact .tel{font-size:26px;margin-top:8px;display:flex;align-items:center;gap:10px}
.nav{position:absolute;left:100px;top:140px;width:1000px;height:44px;border-top:2px solid var(--ink);border-bottom:2px solid var(--ink);display:flex;justify-content:space-between;align-items:center;padding:0 8px;font-family:"Noto Serif",serif;font-size:15px;font-weight:700}
.nav span{line-height:1.05;text-align:center}
.hero-photo{position:absolute;left:100px;top:196px;width:580px;height:340px;background:linear-gradient(120deg,#9a9a9a,#3b3b3b 60%,#1a1a1a)}
.news{position:absolute;left:700px;top:212px;width:400px}
.tabs{display:flex;justify-content:center;gap:12px}
.tab{width:80px;height:26px;border:1px solid var(--ink);font-size:13px;font-family:"Noto Serif",serif;display:flex;align-items:center;justify-content:center}
.tab.on{background:var(--ink);color:var(--paper)}
.entry{display:flex;gap:20px;padding:22px 0;border-bottom:1px solid var(--line);font-size:12px;line-height:1.6}
.entry .date{font-family:"Noto Serif",serif;font-weight:700;white-space:nowrap}
.more{display:block;margin:22px auto 0;width:160px;border-bottom:1px solid var(--ink);text-align:center;font-family:"Noto Serif",serif;font-weight:700;font-size:15px;padding-bottom:6px}
.section-title{display:inline-block;font-family:"Noto Serif",serif;font-weight:700;font-size:40px;padding:4px 34px;border-top:2px solid var(--ink);border-bottom:2px solid var(--ink)}
.recommend{position:absolute;left:100px;top:560px;width:1000px;height:360px}
.recommend .copy{position:absolute;left:40px;top:10px;width:420px;text-align:center}
.recommend p{margin-top:36px;font-size:14px;line-height:2}
.recommend .more{margin-top:34px}
.rec-photo{position:absolute;right:0;top:6px;width:500px;height:340px;background:linear-gradient(140deg,#aeb59a,#4a4f3d 45%,#151515)}
.insta{position:absolute;left:0;top:932px;width:1200px;height:408px;background:var(--mist);text-align:center;padding-top:24px}
.thumbs{display:flex;justify-content:center;gap:24px;margin-top:40px}
.thumb{width:146px}
.thumb .img{height:120px}
.thumb p{font-size:11px;text-align:left;margin-top:8px;color:var(--muted)}
.btn-row{display:flex;justify-content:center;gap:90px;margin-top:40px}
.btn-row .more{margin:0;width:170px}
.shop{position:absolute;left:100px;top:1360px;width:1000px;height:480px;text-align:center}
.shop-body{display:flex;gap:60px;margin-top:30px;text-align:left;padding-left:60px}
.shop dl{width:520px;font-size:13px;line-height:1.7}
.shop dt{font-weight:700}
.shop dd{margin-bottom:6px}
.shop .pics{display:flex;flex-direction:column;gap:16px}
.shop .pics div{width:240px;height:130px}
.shop .btn-row{gap:110px;margin-top:26px}
.map{position:absolute;left:100px;top:1864px;width:1000px;height:260px;background:linear-gradient(135deg,#d9d9d9,#bdbdbd)}
.band{position:absolute;left:100px;top:2132px;width:1000px;height:330px;background:linear-gradient(90deg,#0b0b0b,#3a3a32 50%,#0b0b0b)}
.footer{position:absolute;left:100px;top:2462px;width:1000px;height:202px;background:var(--ink);color:var(--paper);text-align:center;padding-top:18px}
.footer .brand{position:static;display:inline-flex;color:var(--paper);gap:10px}
.footer .brand-mark{width:16px;height:16px}
.footer .brand-name{font-size:32px}
.footer .addr{font-family:"Noto Serif",serif;font-weight:700;font-size:13px;margin-top:8px}
.footer .tel{font-family:"Noto Serif",serif;font-weight:700;font-size:20px}
.footer .nav{position:static;margin-top:14px;border-color:var(--paper);height:40px;font-size:13px;width:100%}
.copy-note{font-size:10px;margin-top:10px;color:#bbb}
</style>
</head>
<body>
<div class="page">
  <header class="header">
    <div class="brand"><span class="brand-mark"></span><span class="brand-name">VEL</span></div>
    <div class="contact">
      <div class="addr">1F 3-8-21 MINAMI-KOHAMA, OSAKA CITY</div>
      <div class="tel"><svg width="24" height="24" viewBox="0 0 24 24"><path d="M6 3l4 4-2 3c1 3 3 5 6 6l3-2 4 4-3 3C10 20 4 14 3 6z" fill="var(--ink)"/></svg>06 - 5512 - 7730</div>
    </div>
  </header>
  <nav class="nav">
    <span>Menu</span><span>Staff</span><span>Salon</span><span>Shop &amp;<br>News</span><span>Gallery</span><span>Recommend</span><span>Guest<br>Snap</span><span>Recruit</span><span>Access</span><span>Contact</span><span>Calendar</span>
  </nav>

  <div class="hero-photo" role="img" aria-label="Portrait photo of a woman in monochrome salon setting"></div>
  <section class="news">
    <div class="tabs"><span class="tab on">News</span><span class="tab">Blog</span></div>
    <div class="entry"><span class="date">2017.12.17</span><span>新しいカラーメニューのご案内です。冬のスタイルに合う落ち着いた色味をご用意しました。</span></div>
    <div class="entry"><span class="date">2017.12.17</span><span>年末年始の営業日についてお知らせ致します。ご予約はお早めにどうぞ。</span></div>
    <div class="entry"><span class="date">2017.12.17</span><span>スタッフブログを更新しました。おすすめのヘアケアをご紹介しています。</span></div>
    <span class="more">read more.</span>
  </section>

  <section class="recommend">
    <div class="copy">
      <h2 class="section-title">Recommend</h2>
      <p>静かに続く自分らしさを。<br>日々の暮らしに馴染むスタイルを、<br>ひとりひとりの髪質と向き合い、<br>丁寧にお作り致します。<br>大人のための上質なサロン時間を。</p>
      <span class="more">read more.</span>
    </div>
    <div class="rec-photo" role="img" aria-label="Photo of a couple sitting together in soft green light"></div>
  </section>

  <section class="insta">
    <h2 class="section-title">Instagram</h2>
    <div class="thumbs">
      <div class="thumb"><div class="img" role="img" aria-label="Instagram photo, green tones" style="background:linear-gradient(135deg,#2f4a2a,#0e140c)"></div><p>新作スタイル</p></div>
      <div class="thumb"><div class="img" role="img" aria-label="Instagram photo, pale interior" style="background:linear-gradient(135deg,#e8e8e8,#9a9a9a)"></div><p>サロン風景</p></div>
      <div class="thumb"><div class="img" role="img" aria-label="Instagram photo, dark hairstyle" style="background:linear-gradient(135deg,#6a5a4a,#1a1a1a)"></div><p>ボブスタイル</p></div>
      <div class="thumb"><div class="img" role="img" aria-label="Instagram photo, bright backlit scene" style="background:linear-gradient(135deg,#f2f2f2,#b8b8b8)"></div><p>ショート</p></div>
      <div class="thumb"><div class="img" role="img" aria-label="Instagram photo, muted portrait" style="background:linear-gradient(135deg,#8a8a80,#2a2a28)"></div><p>カラー</p></div>
      <div class="thumb"><div class="img" role="img" aria-label="Instagram photo, night scene" style="background:linear-gradient(135deg,#3b4a3a,#0a0a0a)"></div><p>ロング</p></div>
    </div>
    <div class="btn-row"><span class="more">read more.</span><span class="more">Gallery.</span><span class="more">Guest Snap.</span></div>
  </section>

  <section class="shop">
    <h2 class="section-title">Shop Deta</h2>
    <div class="shop-body">
      <dl>
        <dt>住所</dt><dd>〒559-0000 大阪府大阪市住之江区南小浜3-8-21 1F<br>電話 06-5512-7730</dd>
        <dt>営業時間</dt><dd>平日 OPEN 10:00 CLOSE 19:00<br>土日祝 OPEN 9:00 CLOSE 18:00</dd>
        <dt>定休日</dt><dd>毎週月曜日・第1、第3火曜日</dd>
        <dt>取扱商品</dt><dd>ストレート、カラー&amp;パーマ（平日）10：00迄<br>カット&amp;カラー（平日）11：00迄<br>カット（土日祝）17：00迄</dd>
        <dt>クレジットカード</dt><dd>各種お使い頂けます。</dd>
      </dl>
      <div class="pics">
        <div role="img" aria-label="Photo of salon exterior" style="background:linear-gradient(135deg,#8c8c8c,#3a3a3a)"></div>
        <div role="img" aria-label="Photo of salon interior" style="background:linear-gradient(135deg,#d6d0c6,#6e6a62)"></div>
      </div>
    </div>
    <div class="btn-row"><span class="more">Contact.</span><span class="more">Staff.</span><span class="more">Recruit.</span></div>
  </section>

  <div class="map" role="img" aria-label="Street map showing the salon location"></div>
  <div class="band" role="img" aria-label="Wide photo of a couple in dim warm light"></div>

  <footer class="footer">
    <div class="brand"><span class="brand-mark"></span><span class="brand-name">VEL</span></div>
    <div class="addr">1F 3-8-21 MINAMI-KOHAMA, OSAKA CITY</div>
    <div class="tel">06 - 5512 - 7730</div>
    <nav class="nav">
      <span>Menu</span><span>Staff</span><span>Salon</span><span>Shop &amp;<br>News</span><span>Gallery</span><span>Recommend</span><span>Guest<br>Snap</span><span>Recruit</span><span>Access</span><span>Contact</span><span>Calendar</span>
    </nav>
    <div class="copy-note">Copyright ©VEL All Right reserved.</div>
  </footer>
</div>
</body>
</html>
```